Interactive Banner for Maplecrest Elementary School

title :"The Season of Stride”
Slogan: Khao, Khelo, Badho
(Eat, Play, Grow)

Students will place pictures of themselves doing their favorite sport or physical activity so will need space for 200 students.

Banner is around 128 sq feet. Will get exact dimensions.

Banner dimensions Length: 14 ft 9 in Height: 6 ft 9in

The border can be international flags, athletic symbols, etc..

Maybe use watermark athletic symbols in the background

incorporate logo

Target Market(s)

School community and mostly students to bring awareness to a healthy lifestyle

Industry/Entity Type

School

Font styles to use
Serif
Sans Serif

Requirements
Must have
• Space for photograph of children
• "The Season of Stride”
• Khao, Khelo, Badho
• (Eat, Play, Grow)
• Use our color palate listed. see below.
Nice to have
• international flag border

```html
<!DOCTYPE html>
<html lang="en">
<head>
<meta charset="utf-8">
<title>The Season of Stride – Maplecrest Elementary School</title>
<link rel="stylesheet" href="https://fonts.googleapis.com/css2?family=Roboto+Condensed:wght@700;900&display=swap">
<style>
  :root{
    --green:#134a33;
    --gold:#b4984f;
    --gold-light:#e6d9b4;
    --box-line:#cdb883;
    --paper:#ffffff;
    --frame:#d7d7d7;
    --flag-red:#c8262c;
    --flag-green:#2f8a3e;
    --flag-blue:#1f3f8f;
    --flag-yellow:#f0c419;
    --silhouette:#3a3a3a;
  }
  *{box-sizing:border-box;margin:0;padding:0}
  html,body{width:1200px;height:578px;overflow:hidden;background:#fff}
  .banner{position:relative;width:1200px;height:578px;background:var(--paper)}
  .frame{position:absolute;left:20px;top:20px;width:1160px;height:536px;border:1px solid var(--frame)}
  .flag-strip{position:absolute}
  .flag-strip--top,.flag-strip--bottom{
    left:20px;width:1160px;height:24px;
    background:linear-gradient(90deg,var(--flag-green),var(--flag-blue) 12%,var(--flag-red) 25%,var(--flag-green) 38%,var(--flag-blue) 50%,var(--flag-red) 62%,var(--flag-yellow) 75%,var(--flag-red) 88%,var(--flag-blue));
  }
  .flag-strip--top{top:20px}
  .flag-strip--bottom{top:532px}
  .flag-strip--left,.flag-strip--right{
    top:44px;width:24px;height:488px;
    background:linear-gradient(180deg,var(--flag-blue),var(--flag-red) 15%,var(--flag-green) 30%,var(--flag-red) 45%,var(--flag-yellow) 58%,var(--flag-green) 72%,var(--flag-red) 86%,var(--flag-yellow));
  }
  .flag-strip--left{left:20px}
  .flag-strip--right{left:1156px}

  .school-mark{position:absolute;left:54px;top:70px;width:118px;display:flex;flex-direction:column;align-items:center;gap:8px;text-align:center}
  .school-mark__dot{width:40px;height:40px;border-radius:50%;background:var(--gold)}
  .school-mark__name{font-family:'Roboto Condensed',sans-serif;font-weight:700;font-size:14px;line-height:1.15;color:var(--green);text-transform:uppercase}

  .title{position:absolute;left:196px;top:44px;width:940px;font-family:'Roboto Condensed',sans-serif;font-weight:900;font-size:86px;line-height:92px;color:var(--green);text-align:center;white-space:nowrap}

  .slogan-band{position:absolute;left:412px;top:130px;width:520px;height:48px;
    background:linear-gradient(90deg,rgba(255,255,255,0),var(--gold) 22%,var(--gold) 65%,var(--gold-light) 92%,rgba(255,255,255,0));
    display:flex;align-items:center;justify-content:center;gap:10px}
  .slogan{font-family:'Roboto Condensed',sans-serif;font-weight:700;font-size:36px;color:#fff;white-space:nowrap}
  .slogan-translation{font-family:'Roboto Condensed',sans-serif;font-weight:700;font-size:15px;color:#fff;white-space:nowrap;padding-top:10px}

  .athletes{position:absolute;top:130px;height:48px;background:linear-gradient(90deg,rgba(58,58,58,.12),rgba(58,58,58,.28),rgba(58,58,58,.12))}
  .athletes--left{left:176px;width:236px}
  .athletes--right{left:932px;width:184px}

  .photo-grid{position:absolute;left:54px;top:198px;width:1092px;display:grid;grid-template-columns:repeat(25,36px);grid-auto-rows:35px;column-gap:8px;row-gap:6.8px}
  .photo-slot{border:1px solid var(--box-line)}
</style>
</head>
<body>
<main class="banner">
  <div class="frame"></div>
  <div class="flag-strip flag-strip--top" role="img" aria-label="Row of international flags"></div>
  <div class="flag-strip flag-strip--bottom" role="img" aria-label="Row of international flags"></div>
  <div class="flag-strip flag-strip--left" role="img" aria-label="Column of international flags"></div>
  <div class="flag-strip flag-strip--right" role="img" aria-label="Column of international flags"></div>

  <div class="school-mark">
    <span class="school-mark__dot"></span>
    <span class="school-mark__name">Maplecrest Elementary School</span>
  </div>

  <h1 class="title">THE SEASON OF STRIDE</h1>

  <div class="athletes athletes--left" role="img" aria-label="Silhouettes of a weightlifter, polo rider, fencer and kayaker"></div>
  <div class="slogan-band">
    <p class="slogan">KHAO, KHELO, BADHO…</p>
    <p class="slogan-translation">(EAT, PLAY, GROW)</p>
  </div>
  <div class="athletes athletes--right" role="img" aria-label="Silhouettes of a footballer, runner, gymnast and volleyball player"></div>

  <div class="photo-grid" aria-label="Spaces for 200 student photos">
    <div class="photo-slot"></div><div class="photo-slot"></div><div class="photo-slot"></div><div class="photo-slot"></div><div class="photo-slot"></div><div class="photo-slot"></div><div class="photo-slot"></div><div class="photo-slot"></div><div class="photo-slot"></div><div class="photo-slot"></div><div class="photo-slot"></div><div class="photo-slot"></div><div class="photo-slot"></div><div class="photo-slot"></div><div class="photo-slot"></div><div class="photo-slot"></div><div class="photo-slot"></div><div class="photo-slot"></div><div class="photo-slot"></div><div class="photo-slot"></div><div class="photo-slot"></div><div class="photo-slot"></div><div class="photo-slot"></div><div class="photo-slot"></div><div class="photo-slot"></div>
    <div class="photo-slot"></div><div class="photo-slot"></div><div class="photo-slot"></div><div class="photo-slot"></div><div class="photo-slot"></div><div class="photo-slot"></div><div class="photo-slot"></div><div class="photo-slot"></div><div class="photo-slot"></div><div class="photo-slot"></div><div class="photo-slot"></div><div class="photo-slot"></div><div class="photo-slot"></div><div class="photo-slot"></div><div class="photo-slot"></div><div class="photo-slot"></div><div class="photo-slot"></div><div class="photo-slot"></div><div class="photo-slot"></div><div class="photo-slot"></div><div class="photo-slot"></div><div class="photo-slot"></div><div class="photo-slot"></div><div class="photo-slot"></div><div class="photo-slot"></div>
    <div class="photo-slot"></div><div class="photo-slot"></div><div class="photo-slot"></div><div class="photo-slot"></div><div class="photo-slot"></div><div class="photo-slot"></div><div class="photo-slot"></div><div class="photo-slot"></div><div class="photo-slot"></div><div class="photo-slot"></div><div class="photo-slot"></div><div class="photo-slot"></div><div class="photo-slot"></div><div class="photo-slot"></div><div class="photo-slot"></div><div class="photo-slot"></div><div class="photo-slot"></div><div class="photo-slot"></div><div class="photo-slot"></div><div class="photo-slot"></div><div class="photo-slot"></div><div class="photo-slot"></div><div class="photo-slot"></div><div class="photo-slot"></div><div class="photo-slot"></div>
    <div class="photo-slot"></div><div class="photo-slot"></div><div class="photo-slot"></div><div class="photo-slot"></div><div class="photo-slot"></div><div class="photo-slot"></div><div class="photo-slot"></div><div class="photo-slot"></div><div class="photo-slot"></div><div class="photo-slot"></div><div class="photo-slot"></div><div class="photo-slot"></div><div class="photo-slot"></div><div class="photo-slot"></div><div class="photo-slot"></div><div class="photo-slot"></div><div class="photo-slot"></div><div class="photo-slot"></div><div class="photo-slot"></div><div class="photo-slot"></div><div class="photo-slot"></div><div class="photo-slot"></div><div class="photo-slot"></div><div class="photo-slot"></div><div class="photo-slot"></div>
    <div class="photo-slot"></div><div class="photo-slot"></div><div class="photo-slot"></div><div class="photo-slot"></div><div class="photo-slot"></div><div class="photo-slot"></div><div class="photo-slot"></div><div class="photo-slot"></div><div class="photo-slot"></div><div class="photo-slot"></div><div class="photo-slot"></div><div class="photo-slot"></div><div class="photo-slot"></div><div class="photo-slot"></div><div class="photo-slot"></div><div class="photo-slot"></div><div class="photo-slot"></div><div class="photo-slot"></div><div class="photo-slot"></div><div class="photo-slot"></div><div class="photo-slot"></div><div class="photo-slot"></div><div class="photo-slot"></div><div class="photo-slot"></div><div class="photo-slot"></div>
    <div class="photo-slot"></div><div class="photo-slot"></div><div class="photo-slot"></div><div class="photo-slot"></div><div class="photo-slot"></div><div class="photo-slot"></div><div class="photo-slot"></div><div class="photo-slot"></div><div class="photo-slot"></div><div class="photo-slot"></div><div class="photo-slot"></div><div class="photo-slot"></div><div class="photo-slot"></div><div class="photo-slot"></div><div class="photo-slot"></div><div class="photo-slot"></div><div class="photo-slot"></div><div class="photo-slot"></div><div class="photo-slot"></div><div class="photo-slot"></div><div class="photo-slot"></div><div class="photo-slot"></div><div class="photo-slot"></div><div class="photo-slot"></div><div class="photo-slot"></div>
    <div class="photo-slot"></div><div class="photo-slot"></div><div class="photo-slot"></div><div class="photo-slot"></div><div class="photo-slot"></div><div class="photo-slot"></div><div class="photo-slot"></div><div class="photo-slot"></div><div class="photo-slot"></div><div class="photo-slot"></div><div class="photo-slot"></div><div class="photo-slot"></div><div class="photo-slot"></div><div class="photo-slot"></div><div class="photo-slot"></div><div class="photo-slot"></div><div class="photo-slot"></div><div class="photo-slot"></div><div class="photo-slot"></div><div class="photo-slot"></div><div class="photo-slot"></div><div class="photo-slot"></div><div class="photo-slot"></div><div class="photo-slot"></div><div class="photo-slot"></div>
    <div class="photo-slot"></div><div class="photo-slot"></div><div class="photo-slot"></div><div class="photo-slot"></div><div class="photo-slot"></div><div class="photo-slot"></div><div class="photo-slot"></div><div class="photo-slot"></div><div class="photo-slot"></div><div class="photo-slot"></div><div class="photo-slot"></div><div class="photo-slot"></div><div class="photo-slot"></div><div class="photo-slot"></div><div class="photo-slot"></div><div class="photo-slot"></div><div class="photo-slot"></div><div class="photo-slot"></div><div class="photo-slot"></div><div class="photo-slot"></div><div class="photo-slot"></div><div class="photo-slot"></div><div class="photo-slot"></div><div class="photo-slot"></div><div class="photo-slot"></div>
  </div>
</main>
</body>
</html>
```